New web design for a service provider in the medical field

We are looking for a new design for our website. We are a company that repairs and sells medical endoscopes. Our customers include doctors and hospitals. Our current website can be found at https://lumenfix.example/en/lumenfix-english.
We need a new web design (without programming) for the following 3 pages:
-Startpage https://lumenfix.example/en/lumenfix-english/
-Used endoscopes https://lumenfix.example/en/used-endoscopes/
-Purchase https://lumenfix.example/en/purchase/
The design should be modern and stylish.
The blue color of the logo should be reflected on the page, but not too intrusive.
I have uploaded the images from the header. If more images are needed, let me know and I will upload them.

Target Market(s)
Doctors and hospitals

```html
<!DOCTYPE html>
<html lang="en">
<head>
<meta charset="utf-8">
<title>LumenFix – Endoscope Repair</title>
<link rel="stylesheet" href="https://fonts.googleapis.com/css2?family=Poppins:wght@400;500;600;700&display=swap">
<style>
:root{
  --blue:#29a6df;
  --blue-deep:#1b74b9;
  --navy:#213c55;
  --navy-dark:#1b3349;
  --ink:#2b2f36;
  --muted:#5b6470;
  --pale:#eaf1f8;
  --white:#ffffff;
}
*{margin:0;padding:0;box-sizing:border-box}
html,body{width:1200px;height:3701px;overflow:hidden}
body{position:relative;font-family:"Poppins",sans-serif;color:var(--ink);background:var(--white)}
.abs{position:absolute}
a{color:inherit;text-decoration:none}
.btn-outline{position:absolute;border:1.5px solid var(--blue-deep);border-radius:20px;color:var(--blue-deep);font-size:11px;font-weight:600;display:flex;align-items:center;justify-content:center;background:var(--white)}
.btn-solid{position:absolute;background:var(--blue);color:var(--white);border-radius:20px;font-weight:600;display:flex;align-items:center;justify-content:center}
.underline{position:absolute;height:3px;width:58px;background:var(--blue-deep)}
.underline::after{content:"";position:absolute;left:64px;top:0;width:3px;height:3px;background:var(--blue-deep);box-shadow:6px 0 0 var(--blue-deep)}

/* header */
.topbar{top:0;left:0;width:1200px;height:68px;background:var(--white)}
.tagline{left:200px;top:17px;font-size:8px;font-weight:600;letter-spacing:.3px}
.toplinks{left:200px;top:38px;font-size:9px;font-weight:500;display:flex;gap:12px}
.lang{left:426px;top:24px;width:52px;height:20px;border:1px solid var(--blue);border-radius:10px;font-size:9px;display:flex;align-items:center;justify-content:center;gap:6px}
.contact-top{left:746px;font-size:9px;display:flex;align-items:center;gap:8px}
.contact-top .ic{width:16px;height:16px;border-radius:50%;background:var(--pale);display:flex;align-items:center;justify-content:center}
.btn-purchase{left:898px;top:19px;width:102px;height:30px;border:1.5px solid var(--ink);border-radius:16px;font-size:11px;font-weight:600;display:flex;align-items:center;justify-content:center}
.navbar{top:68px;left:0;width:1200px;height:30px;background:var(--blue);color:var(--white);font-size:11px;font-weight:500}
.navbar .item{position:absolute;top:8px}
.logo-tab{left:505px;top:40px;width:190px;height:48px;background:var(--white);clip-path:polygon(0 0,100% 0,90% 100%,10% 100%)}
.logo{left:520px;top:10px;width:160px;display:flex;align-items:center;justify-content:center;gap:8px;font-size:19px;font-weight:600;color:var(--blue-deep)}
.logo .dot{width:12px;height:12px;border-radius:50%;background:var(--blue)}

/* hero */
.hero{top:98px;left:0;width:1200px;height:462px;background:radial-gradient(ellipse at 40% 35%,#6b6d70 0%,#3e3f42 45%,#2a2b2e 100%)}
.hero h1{position:absolute;left:0;width:1200px;top:146px;text-align:center;color:var(--white);font-size:33px;line-height:38px;font-weight:600}
.hero .btn-solid{left:538px;top:247px;width:124px;height:26px;font-size:10px}

/* about */
.about-img-main{left:197px;top:598px;width:310px;height:340px;border:2px solid var(--blue);padding:5px}
.about-img-main div,.about-img-small div,.faulty-img div,.decision-img div{width:100%;height:100%}
.about-img-small{left:417px;top:805px;width:170px;height:170px;border:2px solid var(--blue);padding:5px;background:var(--white)}
.about h2{position:absolute;left:645px;top:606px;width:360px;font-size:24px;line-height:31px;font-weight:600;color:var(--blue-deep)}
.about p{position:absolute;left:645px;width:345px;font-size:10px;line-height:16px;color:var(--ink)}

/* brands */
.brands{top:1039px;left:0;width:1200px;height:137px;background:var(--blue)}
.brand{position:absolute;top:37px;width:187px;height:62px;background:var(--white);box-shadow:0 2px 6px rgba(0,0,0,.15);display:flex;align-items:center;justify-content:center;font-size:19px;font-weight:700;color:var(--navy)}

/* services */
.services{top:1176px;left:0;width:1200px;height:594px;background:var(--navy)}
.services h2{position:absolute;left:0;width:1200px;top:55px;text-align:center;color:var(--white);font-size:25px;font-weight:600}
.services p{position:absolute;left:0;width:1200px;top:113px;text-align:center;color:var(--white);font-size:10px;line-height:16px}
.svc-card{position:absolute;top:175px;width:255px;height:240px;background:var(--white)}
.svc-card .photo{height:177px;position:relative}
.svc-card .badge{position:absolute;left:100px;top:62px;width:54px;height:54px;border-radius:50%;background:rgba(30,30,30,.85);display:flex;align-items:center;justify-content:center}
.svc-card h3{position:absolute;left:12px;top:186px;font-size:16px;font-weight:600;color:var(--blue-deep)}
.svc-card small{position:absolute;left:12px;top:213px;font-size:8.5px;font-weight:600}
.svc-card .arrow{position:absolute;right:12px;top:197px;width:30px;height:30px;border-radius:50%;background:var(--navy);display:flex;align-items:center;justify-content:center}
.svc-card .arrow.active{background:var(--blue)}

/* faulty */
.faulty-box{left:205px;top:1875px;width:445px;height:243px;background:var(--pale)}
.faulty-box h2{position:absolute;left:57px;top:55px;font-size:21px;font-weight:600;color:var(--blue-deep)}
.faulty-box .lead{position:absolute;left:57px;top:103px;font-size:12px;font-weight:500}
.faulty-box .sub{position:absolute;left:57px;top:135px;font-size:10px}
.faulty-img{left:553px;top:1765px;width:448px;height:310px;border:2px solid var(--blue);padding:5px;background:var(--white)}

/* values */
.values-band{left:0;top:2193px;width:1200px;height:411px;background:linear-gradient(100deg,#4f6a86 0%,#93a7bd 45%,#c9d5e1 60%,#7d93ab 100%)}
.values-card{left:244px;top:2328px;width:717px;height:348px;background:var(--white);box-shadow:0 6px 24px rgba(0,0,0,.12)}
.values-card h2{position:absolute;left:0;width:717px;top:30px;text-align:center;font-size:21px;font-weight:600;color:var(--blue-deep)}
.value{position:absolute;width:190px}
.value h4{font-size:12px;font-weight:500;color:var(--blue-deep);line-height:15px;padding-left:22px;position:relative}
.value h4 svg{position:absolute;left:0;top:3px}
.value p{font-size:9.5px;line-height:15px;padding-left:22px;margin-top:8px}
.vline{position:absolute;width:1px;background:#dde3ea}
.hline{position:absolute;height:1px;background:#dde3ea}

/* decision */
.decision-img{left:200px;top:2756px;width:274px;height:367px;border:2px solid var(--blue);padding:5px}
.slider-btn{position:absolute;width:26px;height:26px;border-radius:50%;display:flex;align-items:center;justify-content:center}
.decision h2{position:absolute;left:517px;top:2782px;font-size:24px;line-height:31px;font-weight:600;color:var(--blue-deep)}
.feature{position:absolute;left:517px;width:470px}
.feature .circle{position:absolute;left:0;top:0;width:56px;height:56px;border-radius:50%;background:var(--navy);display:flex;align-items:center;justify-content:center}
.feature h3{position:absolute;left:72px;top:0;font-size:16px;font-weight:600;color:var(--blue-deep)}
.feature p{position:absolute;left:72px;top:24px;width:395px;font-size:9.5px;line-height:15px}

/* help */
.help-line{left:325px;width:552px;height:1px;background:#c8ced6}
.help h2{position:absolute;left:0;width:1200px;top:3208px;text-align:center;font-size:33px;font-weight:600;color:var(--ink);letter-spacing:.5px}
.help .btn-solid{left:513px;top:3265px;width:172px;height:36px;font-size:12px}

/* footer */
.footer{left:0;top:3334px;width:1200px;height:367px;background:var(--navy)}
.footer h3{position:absolute;top:100px;font-size:15px;font-weight:500;color:var(--blue)}
.f-item{position:absolute;left:200px;display:flex;gap:14px;color:var(--white);font-size:10px;line-height:13px}
.f-item .ic{flex:none;width:22px;height:22px;border-radius:50%;background:var(--blue);display:flex;align-items:center;justify-content:center}
.f-links{position:absolute;left:423px;top:134px;color:var(--white);font-size:10.5px;line-height:24.5px}
.f-links .current{color:var(--blue);text-decoration:underline}
.map{position:absolute;left:608px;top:115px;width:391px;height:178px;background:linear-gradient(135deg,#eef0f2,#dfe3e7)}
.copyright{position:absolute;left:0;top:316px;width:1200px;height:51px;background:var(--navy-dark)}
.copyright span{position:absolute;left:200px;top:20px;color:var(--white);font-size:9px;font-weight:500}
.copyright u{color:var(--blue)}
.social{position:absolute;top:12px;width:24px;height:24px;border-radius:50%}
.to-top{position:absolute;left:1150px;top:270px;width:34px;height:34px;border-radius:50%;background:var(--blue-deep);display:flex;align-items:center;justify-content:center}
</style>
</head>
<body>

<!-- header -->
<header>
  <div class="abs topbar"></div>
  <div class="abs tagline">CAUSE THE OUTCOME MATTERS</div>
  <nav class="abs toplinks"><a>Pick-Up Order</a><a>About Us</a><a>Contact Us</a></nav>
  <div class="abs lang">EN <svg width="7" height="5" viewBox="0 0 7 5"><path d="M0 0h7L3.5 5z" fill="#2b2f36"/></svg></div>
  <div class="abs contact-top" style="top:14px">
    <span class="ic"><svg width="9" height="7" viewBox="0 0 9 7"><rect x=".5" y=".5" width="8" height="6" fill="none" stroke="#29a6df"/><path d="M.5.5l4 3 4-3" fill="none" stroke="#29a6df"/></svg></span>
    <u>info@lumenfix.example</u>
  </div>
  <div class="abs contact-top" style="top:37px">
    <span class="ic"><svg width="9" height="9" viewBox="0 0 9 9"><path d="M2 .5l1.5 2-1 1c.6 1.3 1.6 2.3 3 3l1-1 2 1.5L7.5 8.5C3.8 8.3.7 5.2.5 1.5z" fill="#29a6df"/></svg></span>
    + 49 4000 555 120-0
  </div>
  <a class="abs btn-purchase">Purchase</a>
  <nav class="abs navbar">
    <span class="item" style="left:199px;text-decoration:underline">Home</span>
    <span class="item" style="left:252px">Endoscope Repair</span>
    <span class="item" style="left:375px">Used Endoscopes ⌄</span>
    <span class="item" style="left:723px">Endoscopy Systems</span>
    <span class="item" style="left:856px">Endoscopy Accessories ⌄</span>
  </nav>
  <div class="abs logo-tab"></div>
  <div class="abs logo"><span class="dot"></span>LumenFix</div>
</header>

<!-- hero -->
<section class="abs hero" role="img" aria-label="Close-up photograph of a flexible endoscope control body">
  <h1>Put Your Endoscope In<br>Reliable Hands!</h1>
  <a class="btn-solid">Purchase Request</a>
  <svg class="abs" style="left:0;top:0" width="1200" height="462" viewBox="0 0 1200 462">
    <polygon points="470,410 790,372 1200,430 1200,462" fill="#29a6df"/>
    <polygon points="0,462 0,462 790,380 1200,462" fill="#ffffff"/>
  </svg>
</section>

<!-- about -->
<section class="about">
  <div class="abs about-img-main"><div role="img" aria-label="Photograph of an endoscope control handle with wooden grip" style="background:linear-gradient(135deg,#d9dcdf,#8e9296 60%,#b8895a)"></div></div>
  <div class="abs about-img-small"><div role="img" aria-label="Detail photograph of an endoscope handle" style="background:linear-gradient(135deg,#e4e6e8,#8c9094 55%,#c49565)"></div></div>
  <h2>Endoscope Repairs And Second Hand Endoscopes From LumenFix – Cause the outcome matters!</h2>
  <div class="underline" style="left:645px;top:737px"></div>
  <p style="top:770px">LumenFix is a privileged partner for the start-up facility or optimisation of existing healthcare facilities, doctor's offices and hospitals. The quality and reliability of our products and our offered service are our best advertisement!</p>
  <p style="top:852px">As a result of optimised processes and highly qualified specialists in our company, we can work very quickly and with high quality for your benefit of least possible restrictions in your doctor's office or in your hospital.</p>
  <a class="btn-outline" style="left:645px;top:947px;width:89px;height:28px">About Us</a>
</section>

<!-- brands -->
<section class="abs brands">
  <div class="brand" style="left:302px">Aurelon</div>
  <div class="brand" style="left:507px">Vantix Medical</div>
  <div class="brand" style="left:711px">Kiranon Optics</div>
</section>

<!-- services -->
<section class="abs services">
  <h2>Your Future - Our Service</h2>
  <div class="underline" style="left:571px;top:95px"></div>
  <p>LumenFix GmbH is specialised in the repair and sale of Aurelon, Vantix and Kiranon flexible medical endoscopes.<br>As a service-oriented company, we are at your side with our knowledge and skills!</p>

  <article class="svc-card" style="left:200px">
    <div class="photo" role="img" aria-label="Photograph of endoscopes laid out on a blue surface" style="background:linear-gradient(135deg,#c8d5e6,#8a4a5a 50%,#b7c7dd)">
      <span class="badge"><svg width="24" height="24" viewBox="0 0 24 24" fill="none" stroke="#fff" stroke-width="1.8"><circle cx="12" cy="12" r="4"/><circle cx="12" cy="12" r="9" stroke-dasharray="3 2"/></svg></span>
    </div>
    <h3>Repair</h3><small>ENDOSCOPE REPAIR SERVICE</small>
    <span class="arrow"><svg width="12" height="10" viewBox="0 0 12 10" fill="none" stroke="#fff" stroke-width="1.5"><path d="M0 5h11M7 1l4 4-4 4"/></svg></span>
  </article>
  <article class="svc-card" style="left:473px">
    <div class="photo" role="img" aria-label="Photograph of surgeons holding an endoscope" style="background:linear-gradient(135deg,#5fb0c9,#1e5f78 55%,#8cc5d6)">
      <span class="badge"><svg width="24" height="24" viewBox="0 0 24 24" fill="none" stroke="#fff" stroke-width="1.8"><path d="M3 12l9-9h9v9l-9 9z"/><circle cx="16" cy="8" r="1.5"/></svg></span>
    </div>
    <h3>Sale</h3><small>USED ENDOSCOPES</small>
    <span class="arrow"><svg width="12" height="10" viewBox="0 0 12 10" fill="none" stroke="#fff" stroke-width="1.5"><path d="M0 5h11M7 1l4 4-4 4"/></svg></span>
  </article>
  <article class="svc-card" style="left:745px">
    <div class="photo" role="img" aria-label="Photograph of a stethoscope, glasses and face mask on a grey desk" style="background:linear-gradient(135deg,#b4b8bc,#7f858b 55%,#c5c9cd)">
      <span class="badge"><svg width="24" height="24" viewBox="0 0 24 24" fill="none" stroke="#fff" stroke-width="1.8"><rect x="3" y="5" width="18" height="14" rx="2"/><path d="M3 10h18"/></svg></span>
    </div>
    <h3>Purchase</h3><small>ENDOSCOPE REPAIR SERVICE</small>
    <span class="arrow active"><svg width="12" height="10" viewBox="0 0 12 10" fill="none" stroke="#fff" stroke-width="1.5"><path d="M0 5h11M7 1l4 4-4 4"/></svg></span>
  </article>

  <svg class="abs" style="left:0;top:0" width="1200" height="594" viewBox="0 0 1200 594">
    <polygon points="0,541 467,484 0,594" fill="#29a6df"/>
    <polygon points="467,484 1200,541 1200,594 0,594" fill="#ffffff"/>
  </svg>
</section>

<!-- faulty endoscope -->
<section>
  <div class="abs faulty-box">
    <h2>Faulty Endoscope?</h2>
    <div class="underline" style="left:57px;top:88px;width:50px"></div>
    <div class="lead">We ensure quick and smooth repairs!</div>
    <div class="sub">Simple place a</div>
    <a class="btn-outline" style="left:57px;top:160px;width:114px;height:28px">Pick-Up Order</a>
  </div>
  <div class="abs faulty-img"><div role="img" aria-label="Illustration of an endoscope tip inside a blue tissue tunnel" style="background:radial-gradient(circle at 55% 40%,#6f9fe0,#2b5fb0 55%,#173c7e)"></div></div>
</section>

<!-- values -->
<section>
  <div class="abs values-band" role="img" aria-label="Blurred photograph of an endoscope with cable"></div>
  <div class="abs values-card">
    <h2>Cause The Outcome Matters!</h2>
    <div class="underline" style="left:330px;top:68px;width:40px"></div>

    <div class="vline" style="left:238px;top:112px;height:210px"></div>
    <div class="vline" style="left:478px;top:112px;height:210px"></div>
    <div class="hline" style="left:40px;top:207px;width:637px"></div>

    <div class="value" style="left:43px;top:110px"><h4><svg width="14" height="10" viewBox="0 0 14 10" fill="none" stroke="#29a6df" stroke-width="1.5"><path d="M1 5l4 4 8-8"/></svg>One Company For Everyone</h4><p>We are a service provider for doctors and hospitals!</p></div>
    <div class="value" style="left:265px;top:110px"><h4><svg width="14" height="10" viewBox="0 0 14 10" fill="none" stroke="#29a6df" stroke-width="1.5"><path d="M1 5l4 4 8-8"/></svg>Experience Characteristics Us</h4><p>Our team has many years of experience in the business field!</p></div>
    <div class="value" style="left:500px;top:110px"><h4><svg width="14" height="10" viewBox="0 0 14 10" fill="none" stroke="#29a6df" stroke-width="1.5"><path d="M1 5l4 4 8-8"/></svg>The Product is Close To Our Hearts</h4><p>We repair and sell second hand, flexible endoscopes!</p></div>
    <div class="value" style="left:43px;top:229px"><h4><svg width="14" height="10" viewBox="0 0 14 10" fill="none" stroke="#29a6df" stroke-width="1.5"><path d="M1 5l4 4 8-8"/></svg>Guaranteed Service</h4><p>You receive a six-month warranty on all repairs!</p></div>
    <div class="value" style="left:265px;top:229px"><h4><svg width="14" height="10" viewBox="0 0 14 10" fill="none" stroke="#29a6df" stroke-width="1.5"><path d="M1 5l4 4 8-8"/></svg>Quality Not Quantity</h4><p>Reliability and durability instead of inferior replacements!</p></div>
    <div class="value" style="left:500px;top:229px"><h4><svg width="14" height="10" viewBox="0 0 14 10" fill="none" stroke="#29a6df" stroke-width="1.5"><path d="M1 5l4 4 8-8"/></svg>Services For Everyonet</h4><p>Our service includes the manufacturers Aurelon, Vantix and Kiranon!</p></div>
  </div>
</section>

<!-- decision -->
<section class="decision">
  <div class="abs decision-img"><div role="img" aria-label="Photograph of an endoscope control body on a white background" style="background:linear-gradient(135deg,#e9ecef,#9aa3ab 50%,#2e3338)"></div></div>
  <span class="slider-btn" style="left:463px;top:2955px;background:var(--blue)"><svg width="10" height="8" viewBox="0 0 10 8" fill="none" stroke="#fff" stroke-width="1.4"><path d="M0 4h9M6 1l3 3-3 3"/></svg></span>
  <span class="slider-btn" style="left:463px;top:2987px;background:var(--white)"><svg width="10" height="8" viewBox="0 0 10 8" fill="none" stroke="#29a6df" stroke-width="1.4"><path d="M10 4H1M4 1L1 4l3 3"/></svg></span>

  <h2>LumenFix GmbH,<br>Your Decision For Your Future</h2>
  <div class="underline" style="left:517px;top:2851px"></div>

  <div class="feature" style="top:2868px">
    <span class="circle"><svg width="24" height="24" viewBox="0 0 24 24" fill="none" stroke="#fff" stroke-width="1.7"><path d="M4 20l8-8M14 4l6 6-3 3-6-6zM4 4l5 5M20 20l-6-6"/></svg></span>
    <h3>Fast Repairs</h3>
    <p>Keep potential disruptions in your doctor's office or in your hospital at minimum as a result of optimized processes and highly qualified specialists in our company.</p>
  </div>
  <div class="feature" style="top:2944px">
    <span class="circle"><svg width="24" height="24" viewBox="0 0 24 24" fill="none" stroke="#fff" stroke-width="1.7"><path d="M12 2v10M9 5h4a2 2 0 010 4h-2a2 2 0 000 4h4M3 17c3 0 5 2 9 2s6-2 9-2"/></svg></span>
    <h3>Highly cost efficient</h3>
    <p>Benefit from our first class recommendations and implementation by our experienced staff. Our goals is to find the best solutions together with you at the best lowest price point.</p>
  </div>
  <div class="feature" style="top:3033px">
    <span class="circle"><svg width="24" height="24" viewBox="0 0 24 24" fill="none" stroke="#fff" stroke-width="1.7"><path d="M3 11l9-8 9 8M5 9v11h14V9M10 20v-6h4v6"/></svg></span>
    <h3>On-Site Aervice</h3>
    <p>We will gladly pay you a visit to to carry out analysis and repairs on site. Due to our many years of experience – it doesn't get any faster (whithin a 250 km range)</p>
  </div>
</section>

<!-- help -->
<section class="help">
  <div class="abs help-line" style="top:3187px"></div>
  <h2>HOW CAN WE HELP YOU?</h2>
  <a class="btn-solid">Send us &nbsp;a Message!</a>
  <div class="abs help-line" style="top:3325px"></div>
</section>

<!-- footer -->
<footer class="abs footer">
  <svg class="abs" style="left:0;top:0" width="1200" height="82" viewBox="0 0 1200 82">
    <polygon points="0,0 1200,0 1200,4 770,80 0,0" fill="#ffffff"/>
    <polygon points="770,80 1200,4 1200,26" fill="#29a6df"/>
  </svg>

  <h3 style="left:200px">Conatct Info</h3>
  <div class="f-item" style="top:134px"><span class="ic"><svg width="9" height="12" viewBox="0 0 9 12"><path d="M4.5 0A4.5 4.5 0 000 4.5C0 8 4.5 12 4.5 12S9 8 9 4.5A4.5 4.5 0 004.5 0z" fill="#fff"/></svg></span><span>Lindenweg 14<br>21000 Talbrück<br>Germany</span></div>
  <div class="f-item" style="top:184px"><span class="ic"><svg width="10" height="10" viewBox="0 0 9 9"><path d="M2 .5l1.5 2-1 1c.6 1.3 1.6 2.3 3 3l1-1 2 1.5L7.5 8.5C3.8 8.3.7 5.2.5 1.5z" fill="#fff"/></svg></span><span>+49 4000 555 120-0<br>+49 4000 555 120-1 (FAX)</span></div>
  <div class="f-item" style="top:227px;align-items:center"><span class="ic"><svg width="10" height="8" viewBox="0 0 9 7"><rect x=".5" y=".5" width="8" height="6" fill="none" stroke="#fff"/><path d="M.5.5l4 3 4-3" fill="none" stroke="#fff"/></svg></span><span>info@lumenfix.example</span></div>
  <div class="f-item" style="top:264px"><span class="ic"><svg width="11" height="11" viewBox="0 0 11 11" fill="none" stroke="#fff" stroke-width="1.2"><circle cx="5.5" cy="5.5" r="4.5"/><path d="M5.5 3v3h2"/></svg></span><span>Monday - Friday<br>08:00 – 20:00</span></div>

  <h3 style="left:423px">Quick Links</h3>
  <div class="f-links">
    <div class="current">Informations</div>
    <div>About Us</div>
    <div>Contact Us</div>
    <div>Tos</div>
    <div>Copyrights</div>
    <div>Privacy policy</div>
  </div>

  <div class="map" role="img" aria-label="Street map showing the company location"></div>

  <span class="to-top"><svg width="10" height="12" viewBox="0 0 10 12" fill="none" stroke="#fff" stroke-width="1.5"><path d="M5 12V1M1 5l4-4 4 4"/></svg></span>

  <div class="copyright">
    <span>© Copyright 2022 <u>LumenFix</u>. All Rights Reserved.</span>
    <span class="social" style="left:943px;background:var(--blue)"></span>
    <span class="social" style="left:974px;background:var(--blue-deep)"></span>
  </div>
</footer>

</body>
</html>
```